Expanding Training Company needs a powerpoint template to deliver a consistent professional image

We want to start with a ppt template that is clean and flexible.
We are a small training organisation focusing on personal effectiveness, leadership, management and change. The MD is a New Zealander living in the United Kingdom and loves the idea of the clean green image that NZ has and wants the PowerPoint template to reflect that. We are pragmatic in what we do - everything comes back to performance improvement. Our clients are big players and our presentations need to be as clean, and as professional as theirs. We need a template that is versatile and can have their logos added as necessary.
Our training tends to be very current and as such we would like to use a lot of images and less words/bullets. We have company colours, logos and fonts that we are happy with and will continue to use.

Here are our company values to give you a sense of what we are about…

As a learning organisation we are always looking to continually improve and renew, our material, ideas, and methods, and are continually on the look out for new techniques, interventions and applications that provide measurable results to our clients.

We think life is about people and relationships, and we are prepared to walk away if people don't keep their word, are untrustworthy or lack integrity, as life is just too short to work with arses.
And because we are not arses we admit when we are wrong and make good on our commitments.

For our clients its all about performance and training is a performance enhancer, we aim to provide training excellence tin all its guises that delivers performance and happy clients.

We harness the value of the team, we believe in Interdependence.

We make life easier for our clients and each other.

Flexibility, innovation and future focus/vision are what our clients can count on us for.

Work is one of many of life's great facilitators, we recognise and value the others - its not just about work.

Industry/Entity Type

It Company

Other font styles liked:
• Avenir Next

Colors
abd037
9bcb3c

Requirements
Must have
• A clean look with multiple options for inserting images, tables, videos, text boxes etc
• copyright information
Nice to have
• Slide masters

```html
<!DOCTYPE html>
<html lang="en">
<head>
<meta charset="utf-8">
<title>Verdant Advisory – Presentation Template Overview</title>
<link href="https://fonts.googleapis.com/css2?family=Nunito+Sans:wght@400;600;700;800;900&display=swap" rel="stylesheet">
<style>
  :root{
    --canvas:#e4e4e4;
    --paper:#ffffff;
    --green-deep:#2f9d3e;
    --green:#5db43a;
    --green-brand:#9bcb3c;
    --green-lime:#abd037;
    --orange:#f26522;
    --ink:#3b3b3b;
    --text:#6a6a6a;
    --muted:#9a9a9a;
    --rule:#e3e3e3;
    --row:#f1f1f1;
    --dark:#4a4f55;
    --photo-a:#c7ced4;
    --photo-b:#8e9aa5;
  }
  *{box-sizing:border-box;margin:0;padding:0}
  html,body{width:1200px;height:716px;overflow:hidden;background:var(--canvas)}
  body{font-family:"Nunito Sans",Arial,sans-serif;color:var(--text)}
  .deck{
    width:1200px;height:716px;padding:17px;
    display:grid;grid-template-columns:repeat(5,228px);grid-template-rows:repeat(5,127px);
    column-gap:7px;row-gap:12px;
  }
  .slide{position:relative;overflow:hidden;background:var(--paper);box-shadow:0 1px 3px rgba(0,0,0,.18)}
  .abs{position:absolute}
  .photo{position:absolute;background:linear-gradient(135deg,var(--photo-a),var(--photo-b))}
  .photo.warm{background:linear-gradient(135deg,#d9cfc4,#8f8479)}
  .photo.sky{background:linear-gradient(180deg,#b9d4ea,#6f8fa8)}

  .title{position:absolute;left:10px;top:8px;font-size:7px;font-weight:900;color:var(--ink);letter-spacing:.1px;line-height:1}
  .title::before{content:"";display:block;width:8px;height:1.2px;background:var(--green);margin-bottom:2px}
  .sub{position:absolute;left:10px;top:17px;font-size:3.2px;color:var(--muted)}
  .body{font-size:3.6px;line-height:1.45;color:var(--text)}
  .body ul{padding-left:5px}
  .body ul ul{padding-left:6px}
  .body li{margin-bottom:.8px}
  .body p{margin-bottom:2px}
  .head{font-size:4.3px;font-weight:800;color:var(--ink)}

  .brand{position:absolute;left:8px;bottom:4px;display:flex;align-items:center;gap:2px;font-size:4.2px;font-weight:800;color:var(--green);line-height:1}
  .brand::before{content:"";width:4.5px;height:4.5px;border-radius:50%;background:var(--green)}
  .copyright{position:absolute;left:0;right:0;bottom:4.5px;text-align:center;font-size:2.4px;color:var(--muted)}
  .pagemark{position:absolute;right:7px;bottom:4px;width:4.5px;height:4.5px;border-radius:50%;background:var(--green)}

  .cover-title{position:absolute;font-size:8.5px;font-weight:900;line-height:1.1;color:#fff}
  .cover-sub{font-size:4.5px;font-weight:600;margin-top:1.5px}
  .cover-date{font-size:2.8px;margin-top:5px;font-weight:400;opacity:.9}

  .toc-item{position:absolute;display:flex;gap:3px;align-items:flex-start}
  .toc-num{width:10px;height:6px;background:var(--green);color:#fff;font-size:3.2px;font-weight:800;display:flex;align-items:center;justify-content:center}
  .toc-item .body{font-size:3px;line-height:1.3}
  .toc-item b{color:var(--ink);font-size:3.2px}

  .section{position:absolute;font-size:6px;font-weight:900;line-height:1.1}
  .section small{display:block;font-size:3px;font-weight:400;margin-top:1px}
  .chat{width:7px;height:7px;border-radius:50%;display:flex;align-items:center;justify-content:center;margin-bottom:2px}

  table.sample{position:absolute;left:10px;top:25px;width:208px;border-collapse:collapse;font-size:2.8px;color:var(--text)}
  table.sample th{color:#fff;font-weight:700;text-align:left;padding:1.6px 3px;height:6px}
  table.sample td{padding:2px 3px;height:10px;vertical-align:middle}
  table.sample tr:nth-child(even) td{background:var(--row)}

  .member{position:absolute;top:28px;width:40px;text-align:center}
  .avatar{width:22px;height:22px;border-radius:50%;margin:0 auto 3px;border:1.3px solid var(--green);background:linear-gradient(135deg,var(--photo-a),var(--photo-b))}
  .name{font-size:3.4px;font-weight:800;color:var(--green)}
  .role{font-size:2.8px;color:var(--ink);font-weight:600}
  .member .body{font-size:2.6px;line-height:1.35;margin-top:1px}

  .plan{position:absolute;top:28px;width:58px}
  .plan .photo{position:relative;height:35px}
  .plan .lbl{text-align:center;font-size:3px;font-weight:800;color:var(--ink);margin-top:2px}
  .plan .body{font-size:2.6px;text-align:center;line-height:1.35}
  .plan .bar{height:2.4px;margin-top:3px}

  .tile{position:absolute;color:#fff;font-size:2.8px;line-height:1.3;padding:3px}
  .tile b{display:block;font-size:3.2px}

  .pct{position:absolute;font-size:3.4px;color:var(--ink);line-height:1.05;text-align:center}
  .pct b{display:block;font-size:6px;color:var(--green);font-weight:900}

  .tl-box{position:absolute;width:30px;height:14px;color:#fff;font-size:2.6px;line-height:1.25;padding:1.5px 2px}
  .tl-box b{display:block;font-size:2.9px}

  .icon-dot{width:9px;height:9px;border-radius:50%;background:var(--green);display:flex;align-items:center;justify-content:center;margin:0 auto 2px}
</style>
</head>
<body>
<main class="deck">

  <!-- Title option 1 -->
  <section class="slide">
    <div class="photo" role="img" aria-label="Business people working together at a laptop" style="left:70px;top:0;width:158px;height:127px"></div>
    <div class="abs" style="left:60px;top:0;width:70px;height:127px;background:linear-gradient(90deg,#fff,rgba(255,255,255,0))"></div>
    <div class="cover-title" style="left:10px;top:38px;color:var(--green-deep)">PRESENTATION TITLE<div class="cover-sub" style="color:var(--ink)">Subtitle Goes Here</div><div class="cover-date" style="color:var(--text)">March, 2017</div></div>
    <div class="brand" style="font-size:7px;left:10px;bottom:9px">verdant advisory</div>
  </section>

  <!-- Title option 2 -->
  <section class="slide">
    <div class="photo" role="img" aria-label="Business people working together at a laptop" style="inset:0"></div>
    <div class="abs" style="inset:0;background:linear-gradient(90deg,var(--green) 0%,var(--green) 45%,rgba(155,203,60,.55) 70%,rgba(155,203,60,.15) 100%)"></div>
    <div class="cover-title" style="left:12px;top:36px">PRESENTATION TITLE<div class="cover-sub">Subtitle Goes Here</div><div class="cover-date">March, 2017</div></div>
  </section>

  <!-- Title option 3 -->
  <section class="slide">
    <div class="photo" role="img" aria-label="Business people working together at a laptop" style="inset:0"></div>
    <div class="abs" style="inset:0;background:linear-gradient(90deg,rgba(93,180,58,.35) 0%,rgba(93,180,58,.6) 40%,var(--green) 60%,var(--green-brand) 100%)"></div>
    <div class="cover-title" style="left:112px;top:40px">PRESENTATION TITLE<div class="cover-sub">Subtitle Goes Here</div><div class="cover-date">March, 2017</div></div>
  </section>

  <!-- Title option 4 -->
  <section class="slide" style="background:linear-gradient(90deg,var(--green-deep),var(--green-lime))">
    <div class="photo" role="img" aria-label="Business people working together, in a circular frame" style="left:-18px;top:5px;width:117px;height:117px;border-radius:50%"></div>
    <div class="cover-title" style="left:112px;top:40px">PRESENTATION TITLE<div class="cover-sub">Subtitle Goes Here</div><div class="cover-date">March, 2017</div></div>
  </section>

  <!-- Title option 5 -->
  <section class="slide">
    <div class="photo" role="img" aria-label="Business people working together, faded" style="left:0;top:0;width:130px;height:127px;opacity:.45"></div>
    <div class="abs" style="left:60px;top:0;width:80px;height:127px;background:linear-gradient(90deg,rgba(255,255,255,0),#fff)"></div>
    <div class="cover-title" style="left:124px;top:40px;color:var(--green-deep)">PRESENTATION TITLE<div class="cover-sub" style="color:var(--ink)">Subtitle Goes Here</div><div class="cover-date" style="color:var(--text)">March, 2017</div></div>
  </section>

  <!-- Table of content -->
  <section class="slide">
    <div class="title">TABLE OF CONTENT</div><div class="sub">Subtitle Goes Here</div>
    <div class="toc-item" style="left:12px;top:30px"><div class="toc-num">01</div><div class="body"><b>Lorem Ipsum</b><br>1. Lorem ipsum dolor sit amet<br>2. Consectetur adipiscing elit</div></div>
    <div class="toc-item" style="left:12px;top:52px"><div class="toc-num">02</div><div class="body"><b>Lorem Ipsum</b><br>1. Lorem ipsum dolor sit amet<br>2. Consectetur adipiscing elit</div></div>
    <div class="toc-item" style="left:12px;top:74px"><div class="toc-num">03</div><div class="body"><b>Lorem Ipsum</b><br>1. Lorem ipsum dolor sit amet<br>2. Consectetur adipiscing elit</div></div>
    <div class="toc-item" style="left:118px;top:30px"><div class="toc-num">04</div><div class="body"><b>Lorem Ipsum</b><br>1. Lorem ipsum dolor sit amet<br>2. Consectetur adipiscing elit</div></div>
    <div class="toc-item" style="left:118px;top:52px"><div class="toc-num">05</div><div class="body"><b>Lorem Ipsum</b><br>1. Lorem ipsum dolor sit amet<br>2. Consectetur adipiscing elit</div></div>
    <div class="toc-item" style="left:118px;top:74px"><div class="toc-num">06</div><div class="body"><b>Lorem Ipsum</b><br>1. Lorem ipsum dolor sit amet<br>2. Consectetur adipiscing elit</div></div>
    <div class="brand">verdant advisory</div><div class="copyright">© 2017 Verdant Advisory. All rights reserved.</div><div class="pagemark"></div>
  </section>

  <!-- One column -->
  <section class="slide">
    <div class="title">ONE COULUMN</div><div class="sub">Subtitle Goes Here</div>
    <div class="abs body" style="left:10px;top:27px;width:205px">
      <div class="head">Lorem Ipsum</div>
      <ul>
        <li>Lorem ipsum dolor sit amet, te ullum corpora delicata duo. Rebum molestie pri eu. No alia tota modus qui.</li>
        <li>Lorem ipsum dolor sit amet, te ullum corpora delicata duo.
          <ul><li>Sint brute at ius. Duo iisque appareat adversarium at</li><li>Sint brute at ius. Duo iisque appareat adversarium at</li></ul></li>
        <li>Lorem ipsum dolor sit amet, te ullum corpora delicata duo. Rebum molestie pri eu. No alia tota modus qui.</li>
      </ul>
    </div>
    <div class="brand">verdant advisory</div><div class="copyright">© 2017 Verdant Advisory. All rights reserved.</div><div class="pagemark"></div>
  </section>

  <!-- Two column -->
  <section class="slide">
    <div class="title">TWO COULUMN</div><div class="sub">Subtitle Goes Here</div>
    <div class="abs body" style="left:10px;top:27px;width:98px">
      <div class="head">Lorem Ipsum</div>
      <ul><li>Lorem ipsum dolor sit amet, te ullum corpora delicata duo. Rebum molestie pri eu.</li>
        <li>Lorem ipsum dolor sit amet<ul><li>Sint brute at ius. Duo iisque appareat</li></ul></li>
        <li>Lorem ipsum dolor sit amet, te ullum corpora delicata duo. Rebum molestie.</li></ul>
    </div>
    <div class="abs body" style="left:118px;top:27px;width:98px">
      <div class="head">Lorem Ipsum</div>
      <ul><li>Lorem ipsum dolor sit amet, te ullum corpora delicata duo. Rebum molestie pri eu.</li>
        <li>Lorem ipsum dolor sit amet<ul><li>Sint brute at ius. Duo iisque appareat</li></ul></li>
        <li>Lorem ipsum dolor sit amet, te ullum corpora delicata duo. Rebum molestie.</li></ul>
    </div>
    <div class="brand">verdant advisory</div><div class="copyright">© 2017 Verdant Advisory. All rights reserved.</div><div class="pagemark"></div>
  </section>

  <!-- Image and text -->
  <section class="slide">
    <div class="abs" style="left:0;top:0;width:84px;height:127px;background:linear-gradient(160deg,var(--green-deep),var(--green-brand))"></div>
    <div class="abs body" style="left:8px;top:30px;width:68px;color:#fff;font-size:2.8px;opacity:.9">Lorem ipsum dolor sit amet, te ullum corpora delicata duo. Rebum molestie pri eu. No alia tota modus qui. Sint brute at ius, duo iisque appareat.</div>
    <div class="photo" role="img" aria-label="Team meeting around a table" style="left:90px;top:8px;width:66px;height:32px"></div>
    <div class="photo warm" role="img" aria-label="Colleagues in discussion" style="left:159px;top:8px;width:62px;height:32px"></div>
    <div class="photo warm" role="img" aria-label="Workshop participants" style="left:90px;top:43px;width:66px;height:32px"></div>
    <div class="photo" role="img" aria-label="Trainer presenting to a group" style="left:159px;top:43px;width:62px;height:32px"></div>
    <div class="abs" style="left:90px;top:80px;width:130px">
      <div style="font-size:4.4px;font-weight:900;color:var(--green)">Lorem ipsum dolor sit amet,</div>
      <div style="font-size:3px;font-weight:700;color:var(--ink)">sed diam nonumy eirmod, tempor invidunt ut labore</div>
      <div class="body" style="font-size:2.7px">Lorem ipsum dolor sit amet, te ullum corpora delicata duo. Rebum molestie pri eu.</div>
    </div>
    <div class="abs" style="left:90px;top:108px;width:10px;height:1.5px;background:var(--orange)"></div>
  </section>

  <!-- Left column with pyramid -->
  <section class="slide">
    <div class="title">LEFT COULUMN</div><div class="sub">Subtitle Goes Here</div>
    <div class="abs body" style="left:10px;top:27px;width:125px">
      <div class="head">Lorem Ipsum</div>
      <ul><li>Lorem ipsum dolor sit amet, te ullum corpora delicata duo. Rebum molestie pri eu.</li>
        <li>Lorem ipsum dolor sit amet<ul><li>Sint brute at ius. Duo iisque appareat adversarium</li></ul></li>
        <li>Lorem ipsum dolor sit amet, te ullum corpora delicata duo. Rebum molestie pri eu.</li></ul>
    </div>
    <svg class="abs" style="left:152px;top:27px" width="64" height="74" viewBox="0 0 64 74" aria-hidden="true">
      <polygon points="32,0 40.5,17 23.5,17" fill="#8cc63f"/>
      <polygon points="22.5,19 41.5,19 50,36 14,36" fill="#4fae3b"/>
      <polygon points="13,38 51,38 59.5,55 4.5,55" fill="var(--orange)"/>
      <polygon points="3.5,57 60.5,57 64,74 0,74" fill="var(--dark)"/>
    </svg>
    <div class="brand">verdant advisory</div><div class="copyright">© 2017 Verdant Advisory. All rights reserved.</div><div class="pagemark"></div>
  </section>

  <!-- Section break light -->
  <section class="slide">
    <div class="abs" style="left:0;top:0;width:118px;height:127px;background:linear-gradient(135deg,var(--green-deep),var(--green-brand))"></div>
    <div class="section" style="left:128px;top:66px;color:var(--green)">
      <div class="chat" style="background:var(--green)"><svg width="4" height="4" viewBox="0 0 10 10"><path d="M1 1h8v6H4l-2 2V7H1z" fill="#fff"/></svg></div>
      Section Break<small style="color:var(--text)">About Us, Who We are</small>
    </div>
  </section>

  <!-- Section break green -->
  <section class="slide" style="background:linear-gradient(135deg,var(--green-deep),var(--green-lime))">
    <div class="section" style="left:128px;top:66px;color:#fff">
      <div class="chat" style="background:#fff"><svg width="4" height="4" viewBox="0 0 10 10"><path d="M1 1h8v6H4l-2 2V7H1z" fill="var(--green)"/></svg></div>
      Section Break<small>About Us, Who We are</small>
    </div>
  </section>

  <!-- Table sample -->
  <section class="slide">
    <div class="title">TABLE SAMPLE</div><div class="sub">Subtitle Goes Here</div>
    <table class="sample">
      <thead><tr><th style="background:var(--green-deep)">Lorem Ipsum</th><th style="background:var(--green-brand)">Lorem Ipsum 1</th><th style="background:var(--orange)">Lorem Ipsum 2</th><th style="background:var(--dark)">Lorem Ipsum 3</th></tr></thead>
      <tbody>
        <tr><td>Lorem ipsum dolor sit amet, consectetur</td><td>Lorem ipsum dolor sit amet</td><td>Lorem ipsum dolor sit amet</td><td>Lorem ipsum dolor sit amet</td></tr>
        <tr><td>Lorem ipsum dolor sit amet, consectetur</td><td>Lorem ipsum dolor sit amet</td><td>Lorem ipsum dolor sit amet</td><td>Lorem ipsum dolor sit amet</td></tr>
        <tr><td>Lorem ipsum dolor sit amet, consectetur</td><td>Lorem ipsum dolor sit amet</td><td>Lorem ipsum dolor sit amet</td><td>Lorem ipsum dolor sit amet</td></tr>
        <tr><td>Lorem ipsum dolor sit amet, consectetur</td><td>Lorem ipsum dolor sit amet</td><td>Lorem ipsum dolor sit amet</td><td>Lorem ipsum dolor sit amet</td></tr>
        <tr><td>Lorem ipsum dolor sit amet, consectetur</td><td>Lorem ipsum dolor sit amet</td><td>Lorem ipsum dolor sit amet</td><td>Lorem ipsum dolor sit amet</td></tr>
      </tbody>
    </table>
    <div class="brand">verdant advisory</div><div class="copyright">© 2017 Verdant Advisory. All rights reserved.</div><div class="pagemark"></div>
  </section>

  <!-- Our team -->
  <section class="slide">
    <div class="title">OUR TEAM</div><div class="sub">Subtitle Goes Here</div>
    <div class="member" style="left:14px"><div class="avatar" role="img" aria-label="Team member portrait"></div><div class="name">JOHN DOE</div><div class="role">Director &amp; CEO</div><div class="body">Lorem ipsum dolor sit amet, consectetur elit.</div></div>
    <div class="member" style="left:63px"><div class="avatar" role="img" aria-label="Team member portrait"></div><div class="name">JOHN DOE</div><div class="role">Director &amp; CEO</div><div class="body">Lorem ipsum dolor sit amet, consectetur elit.</div></div>
    <div class="member" style="left:112px"><div class="avatar" role="img" aria-label="Team member portrait"></div><div class="name">JOHN DOE</div><div class="role">Director &amp; CEO</div><div class="body">Lorem ipsum dolor sit amet, consectetur elit.</div></div>
    <div class="member" style="left:161px"><div class="avatar" role="img" aria-label="Team member portrait"></div><div class="name">JOHN DOE</div><div class="role">Director &amp; CEO</div><div class="body">Lorem ipsum dolor sit amet, consectetur elit.</div></div>
    <div class="brand">verdant advisory</div><div class="copyright">© 2017 Verdant Advisory. All rights reserved.</div><div class="pagemark"></div>
  </section>

  <!-- Our plan -->
  <section class="slide">
    <div class="title">OUR PLAN</div><div class="sub">Subtitle Goes Here</div>
    <div class="plan" style="left:17px"><div class="photo sky" role="img" aria-label="City skyline at sunrise"></div><div class="lbl">PLAN 1</div><div class="body">Lorem ipsum dolor sit amet, consectetur adipiscing elit sed do.</div><div class="bar" style="background:var(--green-deep)"></div></div>
    <div class="plan" style="left:85px"><div class="photo" role="img" aria-label="Group of people walking outdoors"></div><div class="lbl">PLAN 2</div><div class="body">Lorem ipsum dolor sit amet, consectetur adipiscing elit sed do.</div><div class="bar" style="background:var(--green-brand)"></div></div>
    <div class="plan" style="left:153px"><div class="photo sky" role="img" aria-label="Team celebrating on a hilltop"></div><div class="lbl">PLAN 3</div><div class="body">Lorem ipsum dolor sit amet, consectetur adipiscing elit sed do.</div><div class="bar" style="background:var(--orange)"></div></div>
    <div class="brand">verdant advisory</div><div class="copyright">© 2017 Verdant Advisory. All rights reserved.</div><div class="pagemark"></div>
  </section>

  <!-- Pie chart -->
  <section class="slide">
    <div class="title">PIE CHART SAMPLE</div><div class="sub">Subtitle Goes Here</div>
    <div class="abs" style="left:0;right:0;top:24px;text-align:center;font-size:4.2px;font-weight:800;color:var(--ink)">Lorem ipsum dolor sit amet</div>
    <svg class="abs" style="left:0;top:0" width="228" height="127" aria-hidden="true">
      <g transform="translate(112 64) rotate(-90)">
        <circle r="12.5" fill="none" stroke="var(--green-deep)" stroke-width="25" stroke-dasharray="45.55 78.54"/>
        <circle r="12.5" fill="none" stroke="#8cc63f" stroke-width="25" stroke-dasharray="14.14 78.54" stroke-dashoffset="-45.55"/>
        <circle r="12.5" fill="none" stroke="#c7df6b" stroke-width="25" stroke-dasharray="11 78.54" stroke-dashoffset="-59.69"/>
        <circle r="12.5" fill="none" stroke="var(--orange)" stroke-width="25" stroke-dasharray="4.4 78.54" stroke-dashoffset="-70.69"/>
        <circle r="12.5" fill="none" stroke="#9d9d9d" stroke-width="25" stroke-dasharray="3.45 78.54" stroke-dashoffset="-75.09"/>
      </g>
      <text x="118" y="70" font-size="4" fill="#fff" font-weight="800">58%</text>
      <text x="97" y="74" font-size="3.4" fill="#fff" font-weight="800">18%</text>
      <g stroke="#9a9a9a" stroke-width=".3" fill="none">
        <polyline points="90,52 72,48 62,48"/><polyline points="89,62 74,62 62,62"/><polyline points="90,70 74,78 62,78"/><polyline points="136,56 150,52 160,52"/>
      </g>
      <g font-size="2.8" fill="#6a6a6a">
        <text x="45" y="47">Marketing</text><text x="42" y="61">Business Plan</text><text x="45" y="77">Finance</text><text x="161" y="53">Business Management</text>
      </g>
      <g font-size="2.6" fill="#6a6a6a">
        <rect x="58" y="100" width="3" height="3" fill="var(--green-deep)"/><text x="62.5" y="102.6">Lorem Ipsum</text>
        <rect x="84" y="100" width="3" height="3" fill="#8cc63f"/><text x="88.5" y="102.6">Lorem Ipsum</text>
        <rect x="110" y="100" width="3" height="3" fill="#c7df6b"/><text x="114.5" y="102.6">Lorem Ipsum</text>
        <rect x="136" y="100" width="3" height="3" fill="var(--orange)"/><text x="140.5" y="102.6">Lorem Ipsum</text>
      </g>
    </svg>
    <div class="brand">verdant advisory</div><div class="pagemark"></div>
  </section>

  <!-- Bar chart -->
  <section class="slide">
    <div class="title">BAR CHART SAMPLE</div><div class="sub">Subtitle Goes Here</div>
    <div class="abs" style="left:0;right:0;top:22px;text-align:center;font-size:4.2px;font-weight:800;color:var(--ink)">Lorem ipsum dolor sit amet</div>
    <svg class="abs" style="left:0;top:0" width="228" height="127" aria-hidden="true">
      <g stroke="#e6e6e6" stroke-width=".3"><line x1="28" y1="36" x2="210" y2="36"/><line x1="28" y1="52" x2="210" y2="52"/><line x1="28" y1="68" x2="210" y2="68"/><line x1="28" y1="84" x2="210" y2="84"/></g>
      <line x1="28" y1="100" x2="210" y2="100" stroke="#bbb" stroke-width=".4"/>
      <g font-size="2.6" fill="#9a9a9a"><text x="23" y="37">4</text><text x="23" y="53">3</text><text x="23" y="69">2</text><text x="23" y="85">1</text><text x="23" y="101">0</text></g>
      <rect x="34" y="70" width="6" height="30" fill="var(--green-deep)"/>
      <rect x="48" y="50" width="6" height="50" fill="var(--green-brand)"/>
      <rect x="62" y="76" width="6" height="24" fill="var(--orange)"/>
      <rect x="76" y="44" width="6" height="56" fill="var(--dark)"/>
      <rect x="90" y="60" width="6" height="40" fill="var(--green-deep)"/>
      <rect x="104" y="72" width="6" height="28" fill="var(--green-brand)"/>
      <rect x="118" y="62" width="6" height="38" fill="var(--dark)"/>
      <rect x="132" y="40" width="6" height="60" fill="var(--orange)"/>
      <rect x="146" y="66" width="6" height="34" fill="var(--dark)"/>
      <rect x="160" y="78" width="6" height="22" fill="var(--green-deep)"/>
      <rect x="174" y="72" width="6" height="28" fill="var(--dark)"/>
      <rect x="188" y="56" width="6" height="44" fill="var(--green-brand)"/>
      <g font-size="2.2" fill="#9a9a9a"><text x="32" y="105">Cat 1</text><text x="60" y="105">Cat 3</text><text x="88" y="105">Cat 5</text><text x="116" y="105">Cat 7</text><text x="144" y="105">Cat 9</text><text x="172" y="105">Cat 11</text></g>
    </svg>
    <div class="brand">verdant advisory</div><div class="copyright">© 2017 Verdant Advisory. All rights reserved.</div><div class="pagemark"></div>
  </section>

  <!-- Our result -->
  <section class="slide">
    <div class="title">OUR RESULT</div><div class="sub">Subtitle Goes Here</div>
    <div class="photo" role="img" aria-label="Portrait in black and white" style="left:10px;top:25px;width:40px;height:40px;background:linear-gradient(135deg,#d6d6d6,#7d7d7d)"></div>
    <div class="tile" style="left:52px;top:25px;width:40px;height:40px;background:var(--dark)"><b>Lorem Ipsum</b>Lorem ipsum dolor sit amet elit</div>
    <div class="photo" role="img" aria-label="Portrait in black and white" style="left:94px;top:25px;width:40px;height:40px;background:linear-gradient(135deg,#cfcfcf,#6f6f6f)"></div>
    <div class="tile" style="left:136px;top:25px;width:40px;height:40px;background:var(--orange)"><b>Lorem Ipsum</b>Lorem ipsum dolor sit amet elit</div>
    <div class="photo" role="img" aria-label="Portrait in black and white" style="left:178px;top:25px;width:40px;height:40px;background:linear-gradient(135deg,#dadada,#858585)"></div>
    <div class="tile" style="left:10px;top:67px;width:40px;height:40px;background:var(--green-deep)"><b>Lorem Ipsum</b>Lorem ipsum dolor sit amet elit</div>
    <div class="photo" role="img" aria-label="Portrait in black and white" style="left:52px;top:67px;width:40px;height:40px;background:linear-gradient(135deg,#c9c9c9,#6a6a6a)"></div>
    <div class="tile" style="left:94px;top:67px;width:40px;height:40px;background:var(--green-brand)"><b>Lorem Ipsum</b>Lorem ipsum dolor sit amet elit</div>
    <div class="photo" role="img" aria-label="Portrait in black and white" style="left:136px;top:67px;width:40px;height:40px;background:linear-gradient(135deg,#d2d2d2,#7a7a7a)"></div>
    <div class="tile" style="left:178px;top:67px;width:40px;height:40px;background:var(--green-deep)"><b>Lorem Ipsum</b>Lorem ipsum dolor sit amet elit</div>
    <div class="brand">verdant advisory</div><div class="pagemark"></div>
  </section>

  <!-- Section break photo -->
  <section class="slide">
    <div class="photo" role="img" aria-label="Business people meeting in an office" style="inset:0"></div>
    <div class="abs" style="inset:0;background:linear-gradient(90deg,rgba(93,180,58,.25) 0%,rgba(93,180,58,.75) 45%,var(--green) 70%)"></div>
    <div class="section" style="left:128px;top:66px;color:#fff">
      <div class="chat" style="background:#fff"><svg width="4" height="4" viewBox="0 0 10 10"><path d="M1 1h8v6H4l-2 2V7H1z" fill="var(--green)"/></svg></div>
      Section Break<small>About Us, Who We are</small>
    </div>
  </section>

  <!-- Graphic sample -->
  <section class="slide">
    <div class="title">GRAPHIC SAMPLE</div><div class="sub">Subtitle Goes Here</div>
    <svg class="abs" style="left:0;top:0" width="228" height="127" aria-hidden="true">
      <circle cx="114" cy="66" r="22" fill="none" stroke="#dcdcdc" stroke-width=".5"/>
      <g fill="var(--green)">
        <circle cx="114" cy="44" r="5"/><circle cx="133" cy="55" r="5"/><circle cx="133" cy="77" r="5"/>
        <circle cx="114" cy="88" r="5"/><circle cx="95" cy="77" r="5"/><circle cx="95" cy="55" r="5"/>
      </g>
      <g fill="#fff"><circle cx="114" cy="44" r="1.5"/><circle cx="133" cy="55" r="1.5"/><circle cx="133" cy="77" r="1.5"/><circle cx="114" cy="88" r="1.5"/><circle cx="95" cy="77" r="1.5"/><circle cx="95" cy="55" r="1.5"/></g>
      <g font-size="2.8" fill="#6a6a6a" text-anchor="end"><text x="80" y="44">Lorem ipsum dolor sit amet</text><text x="80" y="47.5">consectetur adipiscing elit</text><text x="80" y="66">Lorem ipsum dolor sit amet</text><text x="80" y="69.5">consectetur adipiscing elit</text><text x="80" y="88">Lorem ipsum dolor sit amet</text><text x="80" y="91.5">consectetur adipiscing elit</text></g>
      <g font-size="2.8" fill="#6a6a6a"><text x="148" y="44">Lorem ipsum dolor sit amet</text><text x="148" y="47.5">consectetur adipiscing elit</text><text x="148" y="66">Lorem ipsum dolor sit amet</text><text x="148" y="69.5">consectetur adipiscing elit</text><text x="148" y="88">Lorem ipsum dolor sit amet</text><text x="148" y="91.5">consectetur adipiscing elit</text></g>
    </svg>
    <div class="brand">verdant advisory</div><div class="copyright">© 2017 Verdant Advisory. All rights reserved.</div><div class="pagemark"></div>
  </section>

  <!-- Content with icons -->
  <section class="slide">
    <div class="photo" role="img" aria-label="Trainer presenting to a seated group" style="left:0;top:0;width:228px;height:56px"></div>
    <div class="abs" style="left:0;top:0;width:228px;height:56px;background:linear-gradient(90deg,rgba(93,180,58,.9),rgba(155,203,60,.35))"></div>
    <div class="abs" style="left:10px;top:9px;font-size:7px;font-weight:900;color:#fff">CONTENT WITH ICONS</div>
    <div class="abs" style="left:10px;top:18px;font-size:3.2px;color:#fff">Subtitle Goes Here</div>
    <div class="abs" style="left:14px;top:62px;width:200px;display:flex;justify-content:space-between;text-align:center">
      <div style="width:44px"><div class="icon-dot"><svg width="5" height="5" viewBox="0 0 10 10"><circle cx="5" cy="5" r="3.5" fill="none" stroke="#fff" stroke-width="1.3"/></svg></div><div style="font-size:3.6px;font-weight:800;color:var(--green)">Lorem Ipsum</div><div class="body" style="font-size:2.6px;line-height:1.3">Lorem ipsum dolor sit amet consectetur elit</div></div>
      <div style="width:44px"><div class="icon-dot"><svg width="5" height="5" viewBox="0 0 10 10"><path d="M2 5l2 2 4-4" fill="none" stroke="#fff" stroke-width="1.4"/></svg></div><div style="font-size:3.6px;font-weight:800;color:var(--green)">Lorem Ipsum</div><div class="body" style="font-size:2.6px;line-height:1.3">Lorem ipsum dolor sit amet consectetur elit</div></div>
      <div style="width:44px"><div class="icon-dot"><svg width="5" height="5" viewBox="0 0 10 10"><rect x="2" y="3" width="6" height="5" fill="#fff"/></svg></div><div style="font-size:3.6px;font-weight:800;color:var(--green)">Lorem Ipsum</div><div class="body" style="font-size:2.6px;line-height:1.3">Lorem ipsum dolor sit amet consectetur elit</div></div>
      <div style="width:44px"><div class="icon-dot"><svg width="5" height="5" viewBox="0 0 10 10"><path d="M5 1v8M1 5h8" stroke="#fff" stroke-width="1.4"/></svg></div><div style="font-size:3.6px;font-weight:800;color:var(--green)">Lorem Ipsum</div><div class="body" style="font-size:2.6px;line-height:1.3">Lorem ipsum dolor sit amet consectetur elit</div></div>
    </div>
    <div class="brand">verdant advisory</div><div class="pagemark"></div>
  </section>

  <!-- World map -->
  <section class="slide">
    <div class="title">WORLD MAP SAMPLE</div><div class="sub">Subtitle Goes Here</div>
    <div class="abs" role="img" aria-label="World map in grey" style="left:42px;top:28px;width:150px;height:74px;border-radius:6px;background:radial-gradient(ellipse at 35% 40%,#cfcfcf 0 30%,transparent 55%),radial-gradient(ellipse at 70% 45%,#cfcfcf 0 35%,transparent 60%),#ececec"></div>
    <div class="pct" style="left:26px;top:42px">North<br>America<b>67%</b></div>
    <div class="pct" style="left:34px;top:78px">South<br>America<b>89%</b></div>
    <div class="pct" style="left:178px;top:38px">Asia<b>79%</b></div>
    <div class="pct" style="left:138px;top:78px">Africa<b>50%</b></div>
    <div class="pct" style="left:186px;top:80px">Australia<b>86%</b></div>
    <div class="abs" style="left:0;right:0;top:108px;text-align:center;font-size:3.2px;color:var(--ink)"><b>Lorem ipsum dolor sit amet</b> consectetur adipiscing elit, sed do eiusmod tempor.</div>
  </section>

  <!-- Timeline -->
  <section class="slide">
    <div class="title">TIMELINE SAMPLE</div><div class="sub">Subtitle Goes Here</div>
    <svg class="abs" style="left:0;top:0" width="228" height="127" aria-hidden="true">
      <line x1="14" y1="70" x2="214" y2="70" stroke="#9a9a9a" stroke-width=".6"/>
      <g fill="#6a6a6a" font-size="3"><text x="14" y="66">2012</text><text x="206" y="66">2017</text></g>
      <g stroke="#9a9a9a" stroke-width=".4"><line x1="60" y1="52" x2="60" y2="70"/><line x1="112" y1="52" x2="112" y2="70"/><line x1="86" y1="70" x2="86" y2="86"/><line x1="140" y1="70" x2="140" y2="86"/></g>
      <g fill="var(--green)"><circle cx="60" cy="70" r="1.4"/><circle cx="86" cy="70" r="1.4"/><circle cx="112" cy="70" r="1.4"/><circle cx="140" cy="70" r="1.4"/></g>
    </svg>
    <div class="tl-box" style="left:45px;top:38px;background:var(--green-deep)"><b>Description 1</b>Lorem ipsum dolor sit amet</div>
    <div class="tl-box" style="left:97px;top:38px;background:var(--orange)"><b>Description 3</b>Lorem ipsum dolor sit amet</div>
    <div class="tl-box" style="left:71px;top:86px;background:var(--green-brand)"><b>Description 2</b>Lorem ipsum dolor sit amet</div>
    <div class="tl-box" style="left:125px;top:86px;background:var(--dark)"><b>Description 4</b>Lorem ipsum dolor sit amet</div>
    <div class="brand">verdant advisory</div><div class="copyright">© 2017 Verdant Advisory. All rights reserved.</div><div class="pagemark"></div>
  </section>

  <!-- Testimonial -->
  <section class="slide">
    <div class="title">TESTIMONIAL SAMPLE</div><div class="sub">Subtitle Goes Here</div>
    <div class="avatar abs" role="img" aria-label="Client portrait" style="left:103px;top:22px;margin:0"></div>
    <div class="abs" style="left:0;right:0;top:47px;text-align:center"><div class="name">JOHN DOE</div><div style="font-size:2.8px;color:var(--text)">Lorem ipsum dolor sit amet, consectetur</div></div>
    <div class="abs body" style="left:20px;top:62px;width:188px;text-align:center;font-size:3px;font-style:normal">“ Lorem Ipsum is simply dummy text of the printing and typesetting industry. Lorem Ipsum has been the industry's standard dummy text ever since the 1500s, when an unknown printer took a galley of type and scrambled it to make a type specimen book. ”</div>
    <div class="abs" style="right:20px;top:92px;font-size:3px;color:var(--ink)">– John Doe</div>
    <div class="brand">verdant advisory</div><div class="pagemark"></div>
  </section>

  <!-- Thank you -->
  <section class="slide" style="background:linear-gradient(135deg,var(--green-deep),var(--green-lime))">
    <div class="photo" role="img" aria-label="Colleagues smiling in a bright office" style="left:0;top:0;width:125px;height:127px"></div>
    <div class="abs" style="left:80px;top:0;width:50px;height:127px;background:linear-gradient(90deg,rgba(93,180,58,0),var(--green))"></div>
    <div class="abs" style="left:130px;top:38px;width:92px;text-align:center;color:#fff;font-size:9px;font-weight:900">THANK YOU</div>
    <div class="abs" style="left:130px;top:58px;width:92px;display:flex;justify-content:space-between;text-align:center;color:#fff;font-size:2.6px">
      <div><svg width="6" height="6" viewBox="0 0 10 10"><path d="M5 1a3 3 0 0 1 3 3c0 2.5-3 5.5-3 5.5S2 6.5 2 4a3 3 0 0 1 3-3z" fill="#fff"/></svg><br><b>ADDRESS</b><br>12 Elm Row, Leeds</div>
      <div><svg width="6" height="6" viewBox="0 0 10 10"><rect x="1" y="2.5" width="8" height="5" fill="none" stroke="#fff"/><path d="M1 2.5l4 3 4-3" fill="none" stroke="#fff"/></svg><br><b>EMAIL</b><br>hello@verdant.co</div>
      <div><svg width="6" height="6" viewBox="0 0 10 10"><rect x="3" y="1" width="4" height="8" rx=".8" fill="none" stroke="#fff"/></svg><br><b>PHONE</b><br>0113 496 0000</div>
    </div>
  </section>

</main>
</body>
</html>
```